Modern Billboard Ad for Criminal Defense Firm

10.5 x 36 We're looking for something to set us apart from the local competition. Looking for sleek and modern. We're a mid-sized firm in a small market city. We want to give the artist room to be creative on this one.
Thanks

Target Market(s)

Adult clients who have been charged with a crime/DWI

Industry/Entity Type

legal

Font styles to use
Serif
Sans Serif

Requirements
Must have
• Needs to have the firm name in large lettering. Law Offices of Marcus T Whitfield. “PLLC” does not have to be included. Phone number of (555) 384-1927 should be included but not the main focus.
Nice to have
• A call to action or something similar. “Don’t go it alone, call today.”, “ Arrested?”

```html
<!DOCTYPE html>
<html lang="en">
<head>
<meta charset="utf-8">
<title>Law Offices of Marcus T Whitfield – Billboard</title>
<link rel="stylesheet" href="https://fonts.googleapis.com/css2?family=Archivo+Black&family=Arimo:wght@700&display=swap">
<style>
  :root {
    --page-bg: #ffffff;
    --frame: #3f4543;
    --board: #ffffff;
    --brand-blue: #1580b8;
    --wave-blue: #4f93c4;
    --wave-light: #a9c9e2;
    --tagline-gray: #7c7c7c;
    --cta-yellow: #f6c200;
    --ink-dark: #3a3a3a;
    --badge-navy: #14294a;
    --badge-sky: #2fa4e7;
  }
  * { margin: 0; padding: 0; box-sizing: border-box; }
  html, body {
    width: 1200px; height: 1200px; overflow: hidden;
    background: var(--page-bg);
  }
  .billboard {
    position: absolute; left: 50px; top: 435px;
    width: 1100px; height: 330px;
    border: 11px solid var(--frame);
    background: var(--board);
    overflow: hidden;
  }
  .wave { position: absolute; inset: 0; width: 100%; height: 100%; }
  .attorney-portrait {
    position: absolute; left: 0; top: 14px;
    width: 270px; height: 294px;
    background: linear-gradient(180deg, #8a8a8a 0%, #5e5e5e 55%, #4a4a4a 100%);
    clip-path: polygon(100px 22px, 122px 0, 178px 0, 200px 22px, 210px 88px, 250px 112px, 270px 294px, 0 294px, 0 170px, 75px 128px, 92px 92px);
  }
  .award-badge {
    position: absolute; left: 18px; top: 22px; z-index: 2;
    width: 53px; height: 74px;
    background: var(--badge-navy);
    border: 2px solid #0b1830;
  }
  .award-badge::before {
    content: ""; position: absolute; left: 0; right: 0; top: 0; height: 16px;
    background: var(--badge-sky);
  }
  .award-badge::after {
    content: ""; position: absolute; left: 0; right: 0; bottom: 0; height: 11px;
    background: var(--badge-sky);
  }
  .firm-name {
    position: absolute; left: 280px; right: 40px; top: 20px;
    text-align: center;
    font-family: "Archivo Black", "Arial Black", sans-serif;
    font-weight: 400;
    font-size: 56px; line-height: 74px;
    color: var(--brand-blue);
    text-transform: uppercase;
    white-space: nowrap;
  }
  .tagline {
    position: absolute; left: 280px; right: 40px; top: 164px;
    text-align: center;
    font-family: "Arimo", Arial, sans-serif; font-weight: 700;
    font-size: 21px; color: var(--tagline-gray);
  }
  .call-button {
    position: absolute; left: 455px; top: 212px;
    width: 416px; height: 68px; border-radius: 34px;
    background: var(--cta-yellow);
    display: flex; align-items: center; justify-content: center; gap: 14px;
  }
  .call-button .phone-icon { width: 38px; height: 38px; flex: none; }
  .call-button .phone-number {
    font-family: "Arimo", Arial, sans-serif; font-weight: 700;
    font-size: 46px; color: var(--ink-dark);
  }
</style>
</head>
<body>
  <section class="billboard" aria-label="Billboard: Law Offices of Marcus T Whitfield">
    <svg class="wave" viewBox="0 0 1078 308" preserveAspectRatio="none" aria-hidden="true">
      <defs>
        <linearGradient id="waveFade" x1="0" y1="0" x2="1" y2="0">
          <stop offset="0" stop-color="#4f93c4"/>
          <stop offset="0.6" stop-color="#4f93c4"/>
          <stop offset="1" stop-color="#dfeaf4"/>
        </linearGradient>
        <linearGradient id="waveLight" x1="0" y1="0" x2="1" y2="0">
          <stop offset="0" stop-color="#a9c9e2"/>
          <stop offset="1" stop-color="#eef4fa"/>
        </linearGradient>
      </defs>
      <path d="M0 140 C 120 180, 250 230, 400 235 C 560 240, 640 190, 780 190 C 900 190, 1000 250, 1078 270 L1078 308 L0 308 Z" fill="url(#waveLight)"/>
      <path d="M0 150 C 140 200, 260 245, 420 248 C 580 250, 660 205, 800 205 C 910 205, 1000 265, 1078 285 L1078 308 L0 308 Z" fill="url(#waveFade)"/>
    </svg>

    <div class="attorney-portrait" role="img" aria-label="Black and white portrait of the attorney holding a suit jacket over his shoulder"></div>
    <div class="award-badge" role="img" aria-label="Community award badge"></div>

    <h1 class="firm-name">Law Offices of<br>Marcus T Whitfield</h1>
    <p class="tagline">“Don’t go it alone, call today.”, “ Arrested?”</p>

    <div class="call-button">
      <svg class="phone-icon" viewBox="0 0 38 38" aria-hidden="true">
        <circle cx="19" cy="19" r="19" fill="#2b2b2b"/>
        <path d="M13.5 10.5c.8-.6 1.9-.4 2.4.4l1.7 2.8c.4.7.3 1.6-.3 2.1l-1.2 1c.9 2 2.5 3.6 4.5 4.5l1-1.2c.5-.6 1.4-.7 2.1-.3l2.8 1.7c.8.5 1 1.6.4 2.4l-1 1.3c-.8 1-2.1 1.4-3.3 1-5.1-1.7-9-5.6-10.7-10.7-.4-1.2 0-2.5 1-3.3z" fill="#ffffff"/>
      </svg>
      <span class="phone-number">(555) 384-1927</span>
    </div>
  </section>
</body>
</html>
```